Ferncastle Financial - Website Design

We need a website design for a new commercial real estate company called Ferncastle Financial. We're effectively commercial mortgage brokers connecting real estate investors to lenders. We need a website that is simple (not busy), elegant, professional, and user-friendly. A lot of the users will be in their 50's and less tech savvy, so a stream-lined design is best. The website will serve as a portal for lenders to review new financing opportunities, as well as for real estate investors to review terms from lenders.
Updates
Just uploaded our logo.
Target Market(s)
Commercial real estate investors and lenders
Industry/Entity Type
Real Estate
Number of Pages Required
1 page
Colors
Designer to choose colors to be used in the design.
Look and feel

```html
<!DOCTYPE html>
<html lang="en">
<head>
<meta charset="utf-8">
<title>Ferncastle Financial</title>
<link rel="stylesheet" href="https://fonts.googleapis.com/css2?family=Bitter:wght@400;500&family=Raleway:wght@400;500&family=Roboto:wght@400;500&display=swap">
<style>
  :root {
    --navy: #1b2a47;
    --navy-deep: #15223b;
    --navy-band: rgba(27, 45, 79, 0.88);
    --gold: #f6b80f;
    --white: #ffffff;
    --ink: #1d1d1d;
    --muted: #b6bfcc;
    --tile-bg: #eef0f3;
  }
  * { box-sizing: border-box; margin: 0; padding: 0; }
  html, body { width: 954px; height: 1200px; overflow: hidden; background: var(--white); }
  body { position: relative; font-family: "Raleway", sans-serif; color: var(--ink); }
  .abs { position: absolute; }

  /* Header */
  .site-header { position: absolute; left: 0; top: 0; width: 954px; height: 91px; background: var(--white); }
  .brand { position: absolute; left: 0; top: 0; width: 126px; height: 91px; background: var(--navy);
           display: flex; flex-direction: column; align-items: center; justify-content: center; gap: 6px; }
  .brand-mark { width: 30px; height: 30px; border-radius: 50%; background: var(--white); }
  .brand-name { font-family: "Bitter", serif; font-size: 10px; letter-spacing: 1px; color: var(--white); text-align: center; line-height: 12px; text-transform: uppercase; }
  .nav a { position: absolute; top: 29px; height: 33px; line-height: 33px; font-family: "Bitter", serif; font-size: 15px; color: var(--ink); text-decoration: none; letter-spacing: 0.3px; }
  .nav a.active { left: 142px; width: 100px; background: var(--gold); color: var(--white); border-radius: 17px; text-align: center; }
  .search-icon { position: absolute; left: 849px; top: 36px; }
  .login { position: absolute; left: 881px; top: 34px; width: 56px; height: 22px; background: var(--navy); color: var(--white);
           font-family: "Bitter", serif; font-size: 11px; line-height: 22px; text-align: center; }

  /* Hero */
  .hero { position: absolute; left: 0; top: 91px; width: 954px; height: 285px;
          background: linear-gradient(100deg, #4d5c74 0%, #6d7a8d 25%, #3f5070 50%, #5a5a62 75%, #6e6a68 100%); }
  .hero-title { position: absolute; left: 0; width: 954px; top: 119px; text-align: center; font-family: "Bitter", serif; font-size: 24px; color: var(--white); }
  .hero-text { position: absolute; left: 260px; width: 434px; top: 164px; text-align: center; font-size: 12px; line-height: 22px; color: var(--white); }

  .quick-search { position: absolute; left: 0; top: 376px; width: 954px; height: 84px; background: var(--navy-band); }
  .qs-label { position: absolute; left: 0; width: 954px; top: 16px; text-align: center; font-size: 12px; color: var(--white); }
  .select { position: absolute; top: 42px; height: 28px; background: var(--white); font-size: 12px; color: #9a9a9a; line-height: 28px; padding-left: 7px; }
  .select::after { content: ""; position: absolute; right: 8px; top: 12px; border-left: 4px solid transparent; border-right: 4px solid transparent; border-top: 5px solid #222; }
  .search-btn { position: absolute; left: 719px; top: 42px; width: 118px; height: 28px; background: var(--gold); color: var(--white); font-size: 12px; line-height: 28px; text-align: center; letter-spacing: 0.5px; }

  /* Property tiles */
  .tiles { position: absolute; left: 0; top: 460px; width: 954px; height: 388px;
           background: radial-gradient(ellipse at 50% 40%, #e6e9ed 0%, #f4f5f7 60%, #fbfbfc 100%); }
  .tile { position: absolute; width: 178px; height: 121px; box-shadow: 0 8px 8px -4px rgba(0,0,0,0.35);
          background: linear-gradient(160deg, #c9c9c9, #8e8e8e); }
  .tile.office { background: linear-gradient(150deg, #2d5c7c, #4a8fb0 45%, #1d3b52); }
  .tile-label { position: absolute; left: 0; right: 0; top: 48px; text-align: center; font-family: "Roboto", sans-serif; font-size: 20px; color: var(--white); letter-spacing: 0.5px; }

  /* Footer */
  .site-footer { position: absolute; left: 0; top: 848px; width: 954px; height: 322px; background: var(--navy); color: var(--white); }
  .col-title { position: absolute; top: 50px; font-family: "Roboto", sans-serif; font-size: 14px; letter-spacing: 0.3px; }
  .col-text { position: absolute; font-size: 12px; line-height: 19px; }
  .links { position: absolute; left: 305px; top: 74px; list-style: none; font-size: 12px; line-height: 20.6px; }
  .news-date { position: absolute; font-size: 11.5px; color: var(--muted); }
  .view-all { position: absolute; font-size: 12px; }
  .footer-brand { position: absolute; left: 56px; top: 192px; width 160px; text-align: center; }
  .footer-mark { width: 64px; height: 64px; border-radius: 50%; background: var(--white); margin: 0 auto 12px; }
  .footer-name { font-family: "Bitter", serif; font-size: 15px; letter-spacing: 2px; text-transform: uppercase; line-height: 19px; }
  .avatar { position: absolute; left: 734px; top: 77px; width: 33px; height: 33px; border-radius: 50%; background: var(--white); border: 5px solid var(--navy); box-shadow: 0 0 0 2px var(--white); }
  .follow { position: absolute; left: 788px; top: 269px; width: 68px; height: 22px; background: #f2f5f8; border-radius: 3px; font-size: 11px; color: #3c7fb6; line-height: 22px; padding-left: 28px; }
  .follow::before { content: ""; position: absolute; left: 6px; top: 5px; width: 12px; height: 12px; background: #4aa3df; }

  .bottom-bar { position: absolute; left: 0; top: 1170px; width: 954px; height: 30px; background: var(--navy-deep); color: var(--white); font-size: 11.5px; }
  .social { position: absolute; top: 9px; width: 12px; height: 12px; border-radius: 50%; background: var(--white); }
  .bar-text { position: absolute; top: 8px; }
</style>
</head>
<body>

<header class="site-header">
  <div class="brand">
    <div class="brand-mark"></div>
    <div class="brand-name">Ferncastle<br>Financial</div>
  </div>
  <nav class="nav">
    <a class="active" href="#">About Us</a>
    <a href="#" style="left:284px">Services</a>
    <a href="#" style="left:392px">Investor Relations</a>
    <a href="#" style="left:566px">Market Insights</a>
    <a href="#" style="left:718px">Contact Us</a>
  </nav>
  <svg class="search-icon" width="18" height="18" viewBox="0 0 18 18" aria-label="Search">
    <circle cx="7.5" cy="7.5" r="5.5" fill="none" stroke="#333" stroke-width="2"/>
    <line x1="11.5" y1="11.5" x2="16.5" y2="16.5" stroke="#333" stroke-width="2.4" stroke-linecap="round"/>
  </svg>
  <div class="login">LOGIN</div>
</header>

<section class="hero" role="img" aria-label="Photo of a bright living room with sofa, kitchen and large windows overlooking hills">
  <h1 class="hero-title" style="font-weight:400">Search Properties</h1>
  <p class="hero-text">Lorem ipsum dolor sit amet, consectetur adipiscing elit. Sed quis quam quis tortor tempor fringilla. Etiam pulvinar dui purus, nec aliquam erat</p>
</section>

<section class="quick-search">
  <div class="qs-label">QUICK SEARCH</div>
  <div class="select" style="left:117px;width:193px">Property Type</div>
  <div class="select" style="left:314px;width:193px">Select location</div>
  <div class="select" style="left:511px;width:96px">Mini Price</div>
  <div class="select" style="left:611px;width:97px">Max Price</div>
  <div class="search-btn">SEARCH</div>
</section>

<section class="tiles">
  <div class="tile office" style="left:88px;top:47px" role="img" aria-label="Glass office towers seen from below"><span class="tile-label">OFFICE</span></div>
  <div class="tile" style="left:287px;top:47px" role="img" aria-label="Resort building reflected in a pool"></div>
  <div class="tile" style="left:486px;top:47px" role="img" aria-label="Suburban family house with lawn"></div>
  <div class="tile" style="left:686px;top:47px" role="img" aria-label="White apartment buildings"></div>
  <div class="tile" style="left:88px;top:212px" role="img" aria-label="Hotel pool with palm trees"></div>
  <div class="tile" style="left:287px;top:212px" role="img" aria-label="City skyline"></div>
  <div class="tile" style="left:486px;top:212px" role="img" aria-label="Aerial view of an industrial park"></div>
  <div class="tile" style="left:686px;top:212px" role="img" aria-label="Modern building at dusk"></div>
</section>

<footer class="site-footer">
  <h3 class="col-title" style="left:41px;font-weight:400">FERNCASTLE</h3>
  <p class="col-text" style="left:41px;top:74px;width:205px">Lorem ipsum dolor sit amet, consectetur adipiscing elit. Sed quis quam quis tortor tempor fringilla. Lorem ipsum dolor sit amet, consectetur adipiscing elit.</p>
  <div class="footer-brand" style="width:160px">
    <div class="footer-mark"></div>
    <div class="footer-name">Ferncastle<br>Financial</div>
  </div>

  <h3 class="col-title" style="left:304px;font-weight:400">QUICK LINK</h3>
  <ul class="links">
    <li>About Us</li><li>Our Services</li><li>Investor Relations</li><li>Market Insights</li>
    <li>Our People</li><li>Property Types</li><li>Career</li><li>Contact Us</li>
  </ul>

  <h3 class="col-title" style="left:486px;font-weight:400">LATEST NEWS</h3>
  <div class="news-date" style="left:485px;top:76px">13 Nov. 2017</div>
  <p class="col-text" style="left:485px;top:98px;width:190px">Lorem ipsum dolor sit amet, consectetur adipiscing elit. Sed quis quam quis tortor tempor.</p>
  <div class="news-date" style="left:485px;top:178px">05 Nov. 2017</div>
  <p class="col-text" style="left:485px;top:200px;width:190px">Lorem ipsum dolor sit amet, consectetur adipiscing elit. Sed quis quam quis tortor tempor.</p>
  <div class="view-all" style="left:485px;top:276px">VIEW ALL</div>

  <h3 class="col-title" style="left:734px;font-weight:400">CHIRPLINE</h3>
  <div class="avatar"></div>
  <div class="col-text" style="left:784px;top:75px">FERNCASTLE<br>@Ferncastle</div>
  <p class="col-text" style="left:733px;top:124px;width:190px">Lorem ipsum #dolor sit amet, consectetur #adipiscing elit. Sed #quis #quam quis tortor tempor. Lorem ipsum #dolor sit amet, consectetur #adipiscing elit.</p>
  <div class="view-all" style="left:733px;top:233px">VIEW ALL</div>
  <div class="follow">Follow</div>
</footer>

<div class="bottom-bar">
  <span class="social" style="left:51px"></span>
  <span class="social" style="left:92px"></span>
  <span class="social" style="left:133px"></span>
  <span class="social" style="left:175px"></span>
  <span class="bar-text" style="left:363px">COPYRIGHT © 2017 - ALL RIGHT RESERVED</span>
  <span class="bar-text" style="left:737px">PRIVACY POLICY</span>
  <span class="bar-text" style="left:845px">|</span>
  <span class="bar-text" style="left:862px">SITE MAP</span>
</div>

</body>
</html>
```